Rising Paths Web Design

I am starting a new company that will provide LIFE COACHING services - I have tried to design a website, but it's too complicated. Right now, it's just me - I'm the only person that will provide services through the website - I have used artmarket to purchase a logo (see below). I want to be able to update the website myself, but need a template - basic design. Because I am not technologically savvy enough to explain in words - I basically want to have a website that will provide basic information about my services (coaching), a page about me and my background, hopefully scheduling possibilities, and testimonials — also a page for writing/blogs. I bought a website through NetHarbor - so when I have a template, I guess I”d use that - but maybe I’ll need to work with a designer to actually get it up on the internet. I have a head shot that I’ll upload, too.
Target Market(s)
Clients from the independent (private school) world - teachers, administrators
Number of Pages Required
4 page
Look and feel
Each slider illustrates characteristics of the customer's brand and the style your logo design should communicate.

```html
<!DOCTYPE html>
<html lang="en">
<head>
<meta charset="utf-8">
<title>Rising Paths Coaching</title>
<link href="https://fonts.googleapis.com/css2?family=Poppins:wght@400;500;600&family=Raleway:wght@400;500;600;700&display=swap" rel="stylesheet">
<style>
:root{
  --green:#05a88a;
  --green-dark:#04957a;
  --ink:#3a3a3a;
  --muted:#6f6f6f;
  --line:#e9eeed;
  --card:#fbfdfc;
  --white:#ffffff;
}
*{box-sizing:border-box;margin:0;padding:0}
html,body{width:1200px;height:3546px;overflow:hidden;background:var(--white)}
body{position:relative;font-family:"Raleway",sans-serif;color:var(--ink)}
section,header,footer{position:absolute;left:0;width:1200px}
.abs{position:absolute}
a{text-decoration:none}
h1,h2,h3{font-family:"Poppins",sans-serif;color:var(--ink)}
.btn{position:absolute;display:flex;align-items:center;justify-content:center;border-radius:20px;font-family:"Poppins",sans-serif;font-size:12.5px;font-weight:500}
.btn-solid{background:var(--green);color:var(--white)}
.btn-outline{border:1.5px solid var(--green);color:var(--ink);background:rgba(255,255,255,.35)}
.btn-white{background:var(--white);color:var(--ink)}

/* header */
.site-header{top:0;height:82px;background:var(--white);border-bottom:1px solid #f1f1f1}
.brand{left:118px;top:8px;display:flex;align-items:center;gap:8px}
.brand-mark{width:60px;height:60px;border-radius:50%;border:2px solid #8fd3c8}
.brand-name{font-family:"Raleway",sans-serif;font-size:13px;font-weight:600;color:var(--green)}
.main-nav a{position:absolute;top:33px;font-size:11.5px;color:var(--ink)}
.main-nav a.active{font-weight:700}
.social-dot{position:absolute;top:35px;width:11px;height:11px;border-radius:50%;background:var(--ink)}

/* hero */
.hero{top:82px;height:554px}
.hero-photo{position:absolute;inset:0;background:radial-gradient(ellipse at 30% 55%,#fbe9c8 0%,#f3dcb6 30%,transparent 60%),linear-gradient(180deg,#efe5da 0%,#ead9c2 55%,#d9b880 80%,#b39a62 100%)}
.hero-title{left:118px;top:122px;font-size:49px;font-weight:600;line-height:61px;color:#3d3d3d}
.hero-text{left:118px;top:252px;width:400px;font-size:12.5px;line-height:25px;color:#555}

/* about */
.about{top:728px;height:520px}
.portrait{left:118px;top:0;width:420px;height:519px;border-radius:8px;background:linear-gradient(160deg,#e6e4df 0%,#cfc8bc 45%,#b9ab97 70%,#ece9e3 100%)}
.about-title{left:600px;top:44px;font-size:44px;font-weight:600;line-height:60px}
.about-text{left:600px;width:480px;font-size:12.5px;line-height:25px;color:#555}
.badge{position:absolute;top:343px;width:50px;height:50px;border-radius:6px;background:#275a82}
.badge.round{border-radius:50%;background:var(--white);border:4px solid #1aa4c9}

/* services */
.service{position:absolute;top:1303px;width:306px;height:142px;border:1px solid var(--line);border-radius:12px;background:var(--card)}
.service svg{position:absolute;left:22px;top:24px}
.service h3{position:absolute;left:86px;top:22px;font-size:16.5px;font-weight:500;line-height:24px}
.service p{position:absolute;left:86px;top:52px;width:200px;font-size:12.5px;line-height:24px;color:#777}

/* banner */
.banner{left:118px;top:1523px;width:963px;height:218px;border-radius:28px;background:var(--green)}
.banner h2{position:absolute;left:54px;top:38px;font-size:45px;font-weight:600;line-height:58px;color:var(--white)}
.banner p{position:absolute;left:54px;top:100px;width:480px;font-size:12.5px;line-height:25px;color:#e9fbf7}

/* section headings */
.section-title{position:absolute;left:0;width:1200px;text-align:center;font-size:45px;font-weight:600;line-height:54px}
.section-sub{position:absolute;left:0;width:1200px;text-align:center;font-size:14px;line-height:20px;font-family:"Poppins",sans-serif}

/* approach */
.approach{top:1800px;height:330px}
.step{position:absolute;top:138px;width:220px;text-align:center}
.step svg{display:block;margin:0 auto}
.step h3{margin-top:26px;font-family:"Raleway",sans-serif;font-size:17px;font-weight:700}
.step p{margin-top:10px;font-size:12.5px;line-height:24px;color:#777}

/* blog */
.blog{top:2178px;height:611px;background:var(--green)}
.blog .section-title,.blog .section-sub{color:var(--white)}
.post{position:absolute;top:172px;width:289px;height:340px;background:var(--white);border-radius:6px;text-align:center}
.post-photo{position:absolute;left:24px;top:23px;width:242px;height:168px;border-radius:8px}
.post h3{position:absolute;left:0;top:212px;width:100%;font-size:16.5px;font-weight:600;line-height:24px}
.post p{position:absolute;left:30px;top:244px;width:229px;font-size:11.5px;line-height:21px;color:#555}
.post .read{position:absolute;left:0;top:302px;width:100%;font-family:"Poppins",sans-serif;font-size:13px;font-weight:500;color:var(--ink)}
.dots{position:absolute;top:539px;left:575px;display:flex;gap:10px}
.dots span{width:9px;height:9px;border-radius:50%;background:var(--white);opacity:.75}

/* testimonials */
.testimonials{top:2789px;height:544px;background:linear-gradient(180deg,#fbfbfb,#ffffff)}
.quote{position:absolute;top:163px;width:268px;height:309px;border:1px solid var(--line);background:var(--card);text-align:center;display:flex;flex-direction:column;align-items:center;padding:38px 20px 0}
.avatar{width:72px;height:72px;border-radius:50%;flex:none}
.quote h3{margin-top:18px;font-size:16.5px;font-weight:400;line-height:24px}
.quote p{margin-top:8px;font-family:"Poppins",sans-serif;font-size:10.5px;line-height:21px;color:#666}
.quote .by{margin-top:10px;font-family:"Poppins",sans-serif;font-size:11.5px;font-weight:500;line-height:18px}

/* footer */
.site-footer{top:3333px;height:213px;background:var(--green);color:var(--white)}
.ring{position:absolute;top:55px;width:28px;height:28px;border-radius:50%;border:1.5px solid var(--white)}
.ring::after{content:"";position:absolute;left:9px;top:9px;width:7px;height:7px;border-radius:50%;background:var(--white)}
.footer-nav a{position:absolute;top:111px;font-size:11.5px;color:var(--white)}
.copyright{position:absolute;left:0;top:150px;width:1200px;text-align:center;font-size:10px}
</style>
</head>
<body>

<header class="site-header">
  <div class="brand abs"><span class="brand-mark"></span><span class="brand-name">Rising Paths</span></div>
  <nav class="main-nav">
    <a class="active" href="#" style="left:420px">Home</a>
    <a href="#" style="left:495px">About Me</a>
    <a href="#" style="left:592px">Schedule a Appointment</a>
    <a href="#" style="left:769px">Testimonials</a>
    <a href="#" style="left:879px">My Blogs</a>
  </nav>
  <span class="social-dot" style="left:976px" aria-label="Social link"></span>
  <span class="social-dot" style="left:1005px" aria-label="Social link"></span>
  <span class="social-dot" style="left:1037px" aria-label="Social link"></span>
  <span class="social-dot" style="left:1070px" aria-label="Social link"></span>
</header>

<section class="hero">
  <div class="hero-photo" role="img" aria-label="Photo of a woman with arms outstretched in a sunlit meadow"></div>
  <h1 class="hero-title abs">Get Started Now<br>With Life Coaching</h1>
  <p class="hero-text abs">Lorem ipsum dolor sit amet, consectetur adipiscing elit, sed do eiusmod tempor incididunt ut labore et dolore magna aliqua. Ut enim ad minim veniam.</p>
  <a class="btn btn-solid" href="#" style="left:118px;top:362px;width:141px;height:37px">About Me</a>
  <a class="btn btn-outline" href="#" style="left:275px;top:362px;width:222px;height:37px">Schedule a Appointment</a>
</section>

<section class="about">
  <div class="portrait abs" role="img" aria-label="Headshot portrait of the coach"></div>
  <h2 class="about-title abs">Hi, I’m Mara</h2>
  <p class="about-text abs" style="top:114px">Lorem ipsum dolor sit amet, consectetur adipiscing elit, sed do eiusmod tempor incididunt ut labore et dolore magna aliqua. Ut enim ad minim veniam, quis nostrud exercitation ullamco laboris nisi ut aliquip ex ea commodo consequat. Duis aute irure dolor in reprehenderit in voluptate velit esse cillum dolore eu fugiat nulla pariatur. Excepteur sint occaecat cupidatat</p>
  <p class="about-text abs" style="top:247px">Lorem ipsum dolor sit amet, consectetur adipiscing elit, sed do eiusmod tempor incididunt ut labore et dolore magna aliqua. Ut enim ad minim veniam, quis nostrud exercitation ullamco laboris nisi ut aliqui.</p>
  <span class="badge round" style="left:600px" aria-label="Certification badge"></span>
  <span class="badge" style="left:673px" aria-label="Certification badge"></span>
  <span class="badge" style="left:747px" aria-label="Certification badge"></span>
  <a class="btn btn-solid" href="#" style="left:600px;top:431px;width:197px;height:36px">Read More About Me</a>
</section>

<div class="service" style="left:118px">
  <svg width="46" height="52" viewBox="0 0 46 52" fill="none" stroke="#05a88a" stroke-width="1.8"><circle cx="23" cy="20" r="11"/><path d="M18 31v6h10v-6M19 41h8M20 45h6M23 2v4M5 20H1M45 20h-4M9 7l3 3M37 7l-3 3"/></svg>
  <h3>Consultancy &amp; Advicing</h3>
  <p>Lorem ipsum dolor consectetur adipiscing elit, sed do eiusmod tempor incididunt labore.</p>
</div>
<div class="service" style="left:447px">
  <svg width="48" height="48" viewBox="0 0 48 48" fill="none" stroke="#05a88a" stroke-width="1.8"><path d="M3 14h12v-3a3 3 0 016 0v3h8v10h-3a3 3 0 000 6h3v10H3z"/><path d="M29 4h16v18H29"/><path d="M3 28h26"/></svg>
  <h3>Problem solving</h3>
  <p>Lorem ipsum dolor consectetur adipiscing elit, sed do eiusmod tempor incididunt labore.</p>
</div>
<div class="service" style="left:775px">
  <svg width="48" height="48" viewBox="0 0 48 48" fill="none" stroke="#05a88a" stroke-width="1.8"><path d="M4 16h26v18H14l-6 6v-6H4z"/><circle cx="34" cy="13" r="10"/><path d="M31 10a3 3 0 116 1c0 2-3 2-3 4M34 18v1M9 23h16M9 28h12"/></svg>
  <h3>Conferencing &amp; talks</h3>
  <p>Lorem ipsum dolor consectetur adipiscing elit, sed do eiusmod tempor incididunt labore.</p>
</div>

<div class="banner abs">
  <h2>Gain a Successful Life</h2>
  <p>Lorem ipsum dolor sit amet, consectetur adipiscing elit, sed do eiusmod tempor incididunt ut labore et dolore magna aliqua. Ut enim ad minim veniam. Lorem ipsum dolor sit amet, consectetur adipiscing elit.</p>
  <a class="btn btn-white" href="#" style="left:686px;top:128px;width:223px;height:40px">Schedule a Appointment</a>
</div>

<section class="approach">
  <h2 class="section-title" style="top:13px">My approach</h2>
  <p class="section-sub" style="top:70px">My approach to life coaching</p>
  <div class="step" style="left:102px">
    <svg width="56" height="58" viewBox="0 0 56 58" fill="none" stroke="#05a88a" stroke-width="1.8"><path d="M14 56V44C6 40 3 32 5 23 8 10 20 3 32 5c12 2 20 12 18 24l4 8h-5v8c0 4-3 6-7 6h-5v5"/><circle cx="28" cy="25" r="11"/><circle cx="28" cy="25" r="6"/><circle cx="28" cy="25" r="1.5"/><path d="M28 25l12-12M37 12h4v-4"/></svg>
    <h3>Identify your goals</h3>
    <p>Lorem ipsum dolor consectetur adipiscing elit, sed do.</p>
  </div>
  <div class="step" style="left:361px">
    <svg width="62" height="56" viewBox="0 0 62 56" fill="none" stroke="#05a88a" stroke-width="1.8"><path d="M20 2h40v30H48l-6 6v-6H20z"/><path d="M40 24l-7-7a4 4 0 016-5l1 1 1-1a4 4 0 016 5z"/><path d="M16 14A14 14 0 002 28c0 5 2 9 6 12l-2 10 9-6c7 2 14 0 18-5"/></svg>
    <h3>Finding the answers</h3>
    <p>Lorem ipsum dolor consectetur adipiscing elit, sed do.</p>
  </div>
  <div class="step" style="left:619px">
    <svg width="60" height="58" viewBox="0 0 60 58" fill="none" stroke="#05a88a" stroke-width="1.8"><path d="M30 6v46M20 54h20M6 14h48M30 2v4"/><path d="M10 14L3 32h14zM50 14l-7 18h14zM3 32a7 5 0 0014 0M43 32a7 5 0 0014 0"/><circle cx="30" cy="22" r="4"/></svg>
    <h3>Finding the balance</h3>
    <p>Lorem ipsum dolor consectetur adipiscing elit, sed do.</p>
  </div>
  <div class="step" style="left:878px">
    <svg width="60" height="58" viewBox="0 0 60 58" fill="none" stroke="#05a88a" stroke-width="1.8"><path d="M4 54h12V42h12V30h12V18h12V6"/><path d="M48 2h8v8h-8z"/><circle cx="24" cy="14" r="4"/><path d="M24 18l-4 12 8 6M20 30l-8 4M22 22l8-2"/></svg>
    <h3>Achieve success</h3>
    <p>Lorem ipsum dolor consectetur adipiscing elit, sed do.</p>
  </div>
</section>

<section class="blog">
  <h2 class="section-title" style="top:57px">From My Blog</h2>
  <p class="section-sub" style="top:115px">Lorem ipsum dolor sit amet</p>
  <article class="post" style="left:118px">
    <div class="post-photo" role="img" aria-label="Photo of a smiling woman lying on grass with a book" style="background:linear-gradient(160deg,#b9a06a,#8d8a4b 50%,#5f8a3c)"></div>
    <h3>Sed ut perspiciatis unde..</h3>
    <p>Lorem ipsum dolor sit amet, consectetur adipiscing elit, sed do eiusmod.</p>
    <a class="read" href="#">Read More</a>
  </article>
  <article class="post" style="left:455px">
    <div class="post-photo" role="img" aria-label="Photo of people shaking hands in an office meeting" style="background:linear-gradient(160deg,#e9eef1,#cfd6dc 50%,#3b4656)"></div>
    <h3>Sed ut perspiciatis unde..</h3>
    <p>Lorem ipsum dolor sit amet, consectetur adipiscing elit, sed do eiusmod.</p>
    <a class="read" href="#">Read More</a>
  </article>
  <article class="post" style="left:791px">
    <div class="post-photo" role="img" aria-label="Photo of a woman raising her arms in a golden wheat field" style="background:linear-gradient(180deg,#f4efe4,#e6d6b4 55%,#c29a52)"></div>
    <h3>Sed ut perspiciatis unde..</h3>
    <p>Lorem ipsum dolor sit amet, consectetur adipiscing elit, sed do eiusmod.</p>
    <a class="read" href="#">Read More</a>
  </article>
  <div class="dots"><span></span><span></span><span></span></div>
</section>

<section class="testimonials">
  <h2 class="section-title" style="top:56px">Client Testimonials</h2>
  <p class="section-sub" style="top:111px">Lorem ipsum dolor sit amet</p>
  <div class="quote" style="left:180px">
    <div class="avatar" role="img" aria-label="Client portrait" style="background:linear-gradient(160deg,#2d5d86,#c9a574)"></div>
    <h3>Lorem Ipsum Dolor</h3>
    <p>I have literally tried every photo editor out there, and nothing can compete with Snapo. I love all the fonts, stickers and filters. Keep it up Snapo and thanks again!</p>
    <span class="by">Amenda</span>
  </div>
  <div class="quote" style="left:467px">
    <div class="avatar" role="img" aria-label="Client portrait" style="background:linear-gradient(160deg,#e05a2a,#3a2420)"></div>
    <h3>Lorem Ipsum Dolor</h3>
    <p>I have literally tried every photo editor out there, and nothing can compete with Snapo. I love all the fonts, stickers and filters. Keep it up Snapo and thanks again!</p>
    <span class="by">Amenda</span>
  </div>
  <div class="quote" style="left:752px">
    <div class="avatar" role="img" aria-label="Client portrait" style="background:linear-gradient(160deg,#c93a3a,#2c4f86)"></div>
    <h3>Lorem Ipsum Dolor</h3>
    <p>I have literally tried every photo editor out there, and nothing can compete with Snapo. I love all the fonts, stickers and filters. Keep it up Snapo and thanks again!</p>
    <span class="by">Peter</span>
  </div>
</section>

<footer class="site-footer">
  <span class="ring" style="left:520px" aria-label="Social link"></span>
  <span class="ring" style="left:564px" aria-label="Social link"></span>
  <span class="ring" style="left:608px" aria-label="Social link"></span>
  <span class="ring" style="left:652px" aria-label="Social link"></span>
  <nav class="footer-nav">
    <a href="#" style="left:350px">Home</a>
    <a href="#" style="left:424px">About Me</a>
    <a href="#" style="left:519px">Schedule a Appointment</a>
    <a href="#" style="left:693px">Testimonials</a>
    <a href="#" style="left:802px">My Blogs</a>
  </nav>
  <p class="copyright">2022 All rights reserved</p>
</footer>

</body>
</html>
```